Brackenridge Honeyworks Co needs web page design

Need a web design for a ecommerce website for honey wine. We make honeywine (a dessert type wine made with honey). Our initial product is a standard honey wine and pyment and a cyser. We have all our logos and designs but need to place in web design to reflect our product and ecommerce. We want the file labeled "lumora cover logo 2" as the banner for the site.

Target Market(s)

People who drink sweeter wines, dessert wine, or non traditional/non-grape wines. Cizer drinkers. 20-60 years old.

Requirements
Must have
• The "bee button" picture as the button image. The "lm cover 2" image as the page banner. Open, bright feel/coloring. Coloring featuring gold, red colors that reflect our logos. PLEASE USE THE LUMORA COVER 2 AS OR ON LABEL BANNER TOP OF WEB PAGE. Files 2-3-4 and 5 are our first labels. Those are what will be on bottles when we sale them. This should reflect on web page. We will not use file 8 labels but the graphics could be used on website. There for inspiration.
Nice to have
• Reflect the fonts that are on our logos as close as possible.
Should not have
• Not too much black, red, or honey references. We don't want the page to be too saturated with any of those elements. Not cluttered with imagery.

```html
<!DOCTYPE html>
<html lang="en">
<head>
<meta charset="utf-8">
<title>Brackenridge Honeyworks Co — Honey Wine</title>
<link rel="stylesheet" href="https://fonts.googleapis.com/css2?family=Cinzel:wght@400;500&family=Open+Sans:ital,wght@0,400;0,600;1,400&display=swap">
<style>
:root{
  --gold:#f3a935;
  --gold-dark:#c99a2e;
  --wine:#9b1b30;
  --ink:#2b2b2b;
  --text:#555;
  --muted:#8a8a8a;
  --pale:#f7f7f7;
  --footer:#1b1b1b;
  --white:#fff;
}
*{box-sizing:border-box;margin:0;padding:0}
html,body{width:1200px;height:4831px;overflow:hidden}
body{position:relative;background:var(--white);font-family:"Open Sans",Arial,sans-serif;color:var(--text)}
.abs{position:absolute}
.serif{font-family:"Cinzel",Georgia,serif;font-weight:400}

/* header */
.site-header{top:0;left:0;width:1200px;height:124px;background:var(--white)}
.brand{left:112px;top:28px;width:260px;text-align:center;color:var(--wine);font-family:"Cinzel",Georgia,serif;font-size:25px;line-height:1.15;letter-spacing:1px}
.brand .brand-dot{display:inline-block;width:12px;height:12px;border-radius:50%;background:var(--gold);margin-bottom:6px}
.brand small{display:block;font-size:15px;letter-spacing:4px;color:var(--gold)}
.topbar{right:112px;top:17px;font-size:15px;color:var(--ink);display:flex;gap:12px;align-items:center}
.topbar svg{vertical-align:-2px;margin-right:6px}
.main-nav{left:418px;top:74px;display:flex;gap:26px;font-family:"Cinzel",Georgia,serif;font-size:15px;color:var(--ink)}
.main-nav .active{color:var(--gold)}
.nav-tools{left:940px;top:63px;display:flex;gap:8px}
.tool{width:44px;height:44px;border-radius:50%;border:2px solid var(--ink);display:flex;align-items:center;justify-content:center}
.tool.cart{background:var(--gold);border-color:var(--gold)}

/* hero */
.hero{top:124px;left:0;width:1200px;height:600px;background:linear-gradient(180deg,#3d73c9 0%,#6d9be0 35%,#e9eef4 55%,#c7c3bb 75%,#7c7061 100%)}
.hero-title{top:70px;width:1200px;text-align:center;color:var(--white);font-size:68px;letter-spacing:2px}
.hero-sub{top:158px;width:1200px;text-align:center;color:var(--white);font-size:29px;font-weight:600}
.hero-curve{left:0;bottom:0;width:1200px;height:100px}

/* button */
.btn{display:flex;align-items:center;height:56px;border-radius:28px;background:var(--ink);color:var(--white);font-size:17px;font-weight:600;padding:0 24px 0 6px;gap:14px}
.btn .bee{width:46px;height:46px;border-radius:50%;background:radial-gradient(circle at 40% 40%,#e2c46a,var(--gold-dark))}
.hero .btn{left:510px;top:226px}

/* welcome */
.welcome-title{left:108px;top:780px;width:510px;font-size:40px;color:var(--ink);line-height:45px}
.welcome-text{left:110px;top:930px;width:492px;font-size:16px;line-height:27.5px;color:var(--text)}
.welcome .btn{left:112px;top:1089px}
.story-photo{left:673px;top:765px;width:434px;height:418px;background:linear-gradient(135deg,#6b5a46,#b49a78 50%,#4a3a2c)}
.story-tag{left:636px;top:741px;width:105px;height:91px;background:var(--gold);color:var(--white);font-size:21px;text-align:center;line-height:26px;padding-top:20px}

/* products */
.product{left:0;width:1200px;height:548px}
.product.pale{background:var(--pale)}
.product-shot{height:548px;top:0}
.product-name{font-size:40px;color:var(--ink)}
.product-price{font-size:33px;font-weight:600;color:var(--ink)}
.product-text{width:500px;font-size:16px;line-height:27px;color:var(--text)}
.features{display:flex;gap:34px}
.feature{width:116px;text-align:center;font-size:16px;line-height:20px;color:var(--ink)}
.feature .ring{width:88px;height:88px;border-radius:50%;border:3px solid var(--wine);display:flex;align-items:center;justify-content:center;margin:0 auto 8px}
.feature .ring span{width:66px;height:66px;border-radius:50%;border:2px solid var(--gold);display:block;position:relative}
.feature .ring span::after{content:"";position:absolute;left:18px;top:18px;width:26px;height:26px;border-radius:50%;background:var(--gold)}

/* blog */
.section-title{width:1200px;text-align:center;font-size:42px;color:var(--ink)}
.post{width:311px}
.post-image{width:311px;height:211px}
.post-date{position:absolute;left:24px;top:178px;width:52px;height:57px;background:var(--wine);color:var(--white);text-align:center;font-size:14px;line-height:18px;padding-top:6px}
.post-date b{display:block;font-size:22px;line-height:24px}
.post-title{margin-top:40px;font-size:22px;font-weight:600;color:var(--ink);letter-spacing:.3px}
.post-text{margin-top:10px;font-size:15px;line-height:25px;color:var(--muted)}

/* testimonials */
.testimonials{top:3446px;left:0;width:1200px;height:469px;background:linear-gradient(180deg,#f3a935 0%,#f0a52f 70%,#e39b2c 100%)}
.testimonials .section-title{top:60px;color:var(--white)}
.quote{top:148px;left:240px;width:720px;text-align:center;color:var(--white);font-style:italic;font-size:23px;line-height:33px}
.quote-name{top:304px;width:1200px;text-align:center;color:var(--white);font-size:21px}
.dots{top:377px;left:551px;display:flex;gap:8px}
.dots i{display:block;width:28px;height:4px;background:rgba(255,255,255,.45)}
.dots i.on{background:var(--white)}

/* gallery */
.gallery-item{top:4065px;width:238px;height:223px}

/* footer */
.footer-curve{top:4340px;left:0;width:1200px;height:80px}
.site-footer{top:4410px;left:0;width:1200px;height:421px;background:var(--footer);color:var(--white)}
.footer-brand{left:108px;top:80px;width:320px;text-align:center;font-family:"Cinzel",Georgia,serif;font-size:34px;letter-spacing:2px;line-height:38px}
.footer-brand small{display:block;font-size:22px;letter-spacing:8px}
.footer-contact{left:112px;top:210px;font-size:16px;line-height:36px;font-weight:600}
.footer-contact svg{vertical-align:-2px;margin-right:12px}
.footer-head{font-family:"Cinzel",Georgia,serif;font-size:20px;letter-spacing:.5px}
.footer-links{list-style:none;font-size:16px;line-height:29px;margin-top:8px}
.newsletter-text{font-size:16px;line-height:21px;margin-top:10px;width:340px}
.email-field{margin-top:18px;width:368px;height:51px;background:var(--white);border:1px solid #ccc;color:var(--muted);font-size:16px;padding:14px 18px}
.subscribe{margin-top:20px;width:157px;height:54px;border-radius:27px;background:var(--gold);color:var(--white);font-weight:600;font-size:16px;text-align:center;line-height:54px}
.copyright{left:112px;top:370px;font-size:16px}
.socials{right:112px;top:362px;display:flex;gap:8px}
.socials span{width:36px;height:36px;border-radius:50%;border:1.5px solid var(--white);display:flex;align-items:center;justify-content:center;font-size:13px;font-weight:600}
</style>
</head>
<body>

<header class="site-header abs">
  <div class="brand abs"><span class="brand-dot"></span><br>Brackenridge<small>Honeyworks Co</small></div>
  <div class="topbar abs">
    <span><svg width="14" height="14" viewBox="0 0 24 24" fill="#f3a935"><path d="M6.6 10.8a15 15 0 0 0 6.6 6.6l2.2-2.2a1 1 0 0 1 1-.25 11.4 11.4 0 0 0 3.6.6 1 1 0 0 1 1 1V20a1 1 0 0 1-1 1A17 17 0 0 1 3 4a1 1 0 0 1 1-1h3.5a1 1 0 0 1 1 1c0 1.25.2 2.45.6 3.6a1 1 0 0 1-.25 1z"/></svg>1 (555) 014-2290</span>
    <span>|</span>
    <span><svg width="15" height="12" viewBox="0 0 24 18" fill="#f3a935"><path d="M0 0h24v18H0zM2 2v.5l10 7 10-7V2z"/></svg>hello@brackenridgehoney.com</span>
  </div>
  <nav class="main-nav abs"><span class="active">Home</span><span>Our Story</span><span>Our Meads</span><span>Blog</span><span>Contact Us</span></nav>
  <div class="nav-tools abs">
    <span class="tool"><svg width="16" height="16" viewBox="0 0 24 24" fill="none" stroke="#2b2b2b" stroke-width="3"><circle cx="10" cy="10" r="7"/><path d="M15 15l6 6"/></svg></span>
    <span class="tool"><svg width="14" height="16" viewBox="0 0 20 22" fill="#2b2b2b"><circle cx="10" cy="6" r="5"/><path d="M0 22c0-6 4-9 10-9s10 3 10 9z"/></svg></span>
    <span class="tool cart"><svg width="18" height="16" viewBox="0 0 24 22" fill="#fff"><path d="M0 0h4l1 4h19l-3 10H7zM8 17a2.5 2.5 0 1 0 0 5 2.5 2.5 0 0 0 0-5zm10 0a2.5 2.5 0 1 0 0 5 2.5 2.5 0 0 0 0-5z"/></svg></span>
  </div>
</header>

<section class="hero abs" role="img" aria-label="Snow-covered mountain summit with an observatory under a blue sky">
  <h1 class="hero-title abs serif">Brackenridge Honeyworks</h1>
  <p class="hero-sub abs">Made from 100% natural honey!</p>
  <a class="btn abs"><span class="bee"></span>SHOP NOW!</a>
  <svg class="hero-curve abs" viewBox="0 0 1200 100" preserveAspectRatio="none">
    <path d="M0 60 Q600 0 1200 75 L1200 100 L0 100Z" fill="#9b1b30"/>
    <path d="M0 95 Q600 25 1200 95 L1200 100 L0 100Z" fill="#fff"/>
  </svg>
</section>

<section class="welcome">
  <h2 class="welcome-title abs serif">Welcome to<br>Brackenridge<br>Honeyworks Co</h2>
  <p class="welcome-text abs">At vero eos et accusamus et iusto odio dignissimos ducimus qui blanditiis praesentium voluptatum de niti atque corrupti quosis dolores et quas molestias excepturi sint occaecati cupiditatesen provident, simili que sunt in culpa qui officia deserunt mollitiain imi, id est laborum et dolorum fuga.</p>
  <a class="btn abs"><span class="bee"></span>READ MORE</a>
  <div class="story-photo abs" role="img" aria-label="Smiling winemaker raising a glass of wine beside oak barrels"></div>
  <div class="story-tag abs serif">OUR<br>STORY</div>
</section>

<section class="product pale abs" style="top:1262px">
  <div class="product-shot abs" style="left:0;width:490px;background:linear-gradient(90deg,#f7f7f7 0%,#3b2e26 25%,#1f1f1f 40%,#e8d6a0 65%,#f7f7f7 90%)" role="img" aria-label="Honey wine bottle with label, a glass of golden wine and a piece of honeycomb"></div>
  <h2 class="product-name abs serif" style="left:594px;top:58px">Honey Wine</h2>
  <p class="product-price abs" style="left:594px;top:112px">$149</p>
  <p class="product-text abs" style="left:596px;top:170px">At vero eos et accusamus et iusto odio dignissimos ducimus qui blanditiis praesentium voluptatum de.</p>
  <div class="features abs" style="left:582px;top:243px">
    <div class="feature"><div class="ring"><span></span></div>Natural<br>Ingredients</div>
    <div class="feature"><div class="ring"><span></span></div>100% natural<br>honey</div>
    <div class="feature"><div class="ring"><span></span></div>Gluten<br>Free</div>
  </div>
  <a class="btn abs" style="left:596px;top:412px"><span class="bee"></span>SHOP NOW!</a>
</section>

<section class="product abs" style="top:1810px">
  <h2 class="product-name abs serif" style="left:112px;top:52px">Pyment</h2>
  <p class="product-price abs" style="left:112px;top:104px">$149</p>
  <p class="product-text abs" style="left:114px;top:160px;width:410px">At vero eos et accusamus et iusto odio dignissimos ducimus qui blanditiis praesentium voluptatum de.</p>
  <div class="features abs" style="left:100px;top:232px">
    <div class="feature"><div class="ring"><span></span></div>Fresh<br>Grapes</div>
    <div class="feature"><div class="ring"><span></span></div>100% natural<br>honey</div>
    <div class="feature"><div class="ring"><span></span></div>Gluten<br>Free</div>
  </div>
  <a class="btn abs" style="left:112px;top:404px"><span class="bee"></span>SHOP NOW!</a>
  <div class="product-shot abs" style="left:545px;width:505px;background:linear-gradient(90deg,#fff 0%,#8e2340 12%,#1f1f1f 35%,#b3121e 70%,#fff 95%)" role="img" aria-label="Pyment bottle with label, a glass of red wine and a bunch of red grapes"></div>
</section>

<section class="product pale abs" style="top:2348px">
  <div class="product-shot abs" style="left:0;width:490px;background:linear-gradient(90deg,#f7f7f7 0%,#c3222a 15%,#1f1f1f 40%,#eedc9e 65%,#f7f7f7 90%)" role="img" aria-label="Cyser bottle with label, a glass of golden wine and red apples"></div>
  <h2 class="product-name abs serif" style="left:602px;top:68px">Cyser</h2>
  <p class="product-price abs" style="left:602px;top:122px">$149</p>
  <p class="product-text abs" style="left:604px;top:178px">At vero eos et accusamus et iusto odio dignissimos ducimus qui blanditiis praesentium voluptatum de.</p>
  <div class="features abs" style="left:590px;top:250px">
    <div class="feature"><div class="ring"><span></span></div>Fresh<br>Apples</div>
    <div class="feature"><div class="ring"><span></span></div>100% natural<br>honey</div>
    <div class="feature"><div class="ring"><span></span></div>Gluten<br>Free</div>
  </div>
  <a class="btn abs" style="left:604px;top:418px"><span class="bee"></span>SHOP NOW!</a>
</section>

<section class="blog">
  <h2 class="section-title abs serif" style="top:2955px">Latest Blog</h2>
  <article class="post abs" style="left:111px;top:3037px">
    <div class="post-image" style="background:linear-gradient(135deg,#5b3b1c,#c79a4d 55%,#3a2610)" role="img" aria-label="Glasses of white wine on a wooden table"></div>
    <div class="post-date"><b>10</b>MAY</div>
    <h3 class="post-title">Ut enim ad minima venia</h3>
    <p class="post-text">Nemo enim ipsam voluptatem quia volu ptas sit aspernatur aut odit.</p>
  </article>
  <article class="post abs" style="left:444px;top:3037px">
    <div class="post-image" style="background:linear-gradient(180deg,#6b3a2a,#e0843c 40%,#8a5a22 70%,#4a3a14)" role="img" aria-label="Vineyard rows at sunset"></div>
    <div class="post-date"><b>10</b>MAY</div>
    <h3 class="post-title">Ut enim ad minima venia</h3>
    <p class="post-text">Nemo enim ipsam voluptatem quia volu ptas sit aspernatur aut odit.</p>
  </article>
  <article class="post abs" style="left:778px;top:3037px">
    <div class="post-image" style="background:linear-gradient(135deg,#4d5a3a,#b7262c 40%,#e2c27a 70%,#7b8a5a)" role="img" aria-label="Basket of red apples beside a glass of cider"></div>
    <div class="post-date"><b>10</b>MAY</div>
    <h3 class="post-title">Ut enim ad minima venia</h3>
    <p class="post-text">Nemo enim ipsam voluptatem quia volu ptas sit aspernatur aut odit.</p>
  </article>
</section>

<section class="testimonials abs">
  <h2 class="section-title abs serif">Client Testimonials</h2>
  <p class="quote abs">“ Nam libero tempore, cum soluta nobis est eligendi optio cum nihil impedit quo minus id quod maxime placeat facere possimus, om nis voluptas assumenda est, omnis dolor repellendus. Temporibus autem quibusdam et aut officiis debitis au.”</p>
  <p class="quote-name abs">- CLARA WHITFIELD</p>
  <div class="dots abs"><i class="on"></i><i></i><i></i></div>
</section>

<section class="gallery">
  <h2 class="section-title abs serif" style="top:3977px">#BrackenridgeHoneyworks</h2>
  <div class="gallery-item abs" style="left:111px;background:linear-gradient(180deg,#8fa7b8,#6b8a3a 40%,#3d4f1d)" role="img" aria-label="Vineyard rows on rolling hills"></div>
  <div class="gallery-item abs" style="left:358px;background:linear-gradient(135deg,#2a0c10,#9b1522 50%,#f1e6e2)" role="img" aria-label="Red wine pouring into a glass"></div>
  <div class="gallery-item abs" style="left:604px;background:linear-gradient(135deg,#3a4a22,#2e3a6b 50%,#1c2240)" role="img" aria-label="Bunch of dark grapes on the vine"></div>
  <div class="gallery-item abs" style="left:851px;background:linear-gradient(90deg,#8a8f96,#c9ccd0 40%,#b26a52 70%,#3a3a3a)" role="img" aria-label="Cellar worker tasting beside steel tanks"></div>
</section>

<svg class="footer-curve abs" viewBox="0 0 1200 80" preserveAspectRatio="none">
  <path d="M0 10 Q600 70 1200 10 L1200 80 L0 80Z" fill="#9b1b30"/>
  <path d="M0 30 Q600 80 1200 30 L1200 80 L0 80Z" fill="#1b1b1b"/>
</svg>

<footer class="site-footer abs">
  <div class="footer-brand abs">Brackenridge<small>Honeyworks Co</small></div>
  <div class="footer-contact abs">
    <div><svg width="14" height="14" viewBox="0 0 24 24" fill="#f3a935"><path d="M6.6 10.8a15 15 0 0 0 6.6 6.6l2.2-2.2a1 1 0 0 1 1-.25 11.4 11.4 0 0 0 3.6.6 1 1 0 0 1 1 1V20a1 1 0 0 1-1 1A17 17 0 0 1 3 4a1 1 0 0 1 1-1h3.5a1 1 0 0 1 1 1c0 1.25.2 2.45.6 3.6a1 1 0 0 1-.25 1z"/></svg>1 (555) 014-2290 &nbsp;|</div>
    <div><svg width="15" height="12" viewBox="0 0 24 18" fill="#f3a935"><path d="M0 0h24v18H0zM2 2v.5l10 7 10-7V2z"/></svg>hello@brackenridgehoney.com</div>
  </div>
  <div class="abs" style="left:508px;top:70px">
    <h4 class="footer-head">Information</h4>
    <ul class="footer-links"><li>Home</li><li>Our Story</li><li>Our Meads</li><li>Blog</li><li>Contact</li></ul>
  </div>
  <div class="abs" style="left:720px;top:70px">
    <h4 class="footer-head">Newsletter Subscription</h4>
    <p class="newsletter-text">Subscribe and stay on top of our latest news and promotions</p>
    <div class="email-field">Email Address</div>
    <div class="subscribe">SUBSCRIBE</div>
  </div>
  <p class="copyright abs">Copyright © 2021, Brackenridge Honeyworks. All rights reserved.</p>
  <div class="socials abs"><span>lm</span><span></span><span></span></div>
</footer>

</body>
</html>
```